the ridgewell craft premier branch

design a DL A4 tri fold brochure to reflect our creative landscape business
my web site www.theridgewellcraft.com.au
has all the information needed
i will also be updating the website to be more updated and creative design

```html
<!DOCTYPE html>
<html lang="en">
<head>
<meta charset="utf-8">
<title>The Ridgewell Craft – Tri-fold Brochure</title>
<link href="https://fonts.googleapis.com/css2?family=Roboto:wght@300;400;500;700&display=swap" rel="stylesheet">
<style>
  :root {
    --paper: #ffffff;
    --ink: #3a3a3a;
    --ink-dark: #1d1d1b;
    --muted: #7a7a7a;
    --accent: #f39200;
    --on-photo: #ffffff;
  }
  * { box-sizing: border-box; margin: 0; padding: 0; }
  html, body { width: 1200px; height: 848px; overflow: hidden; background: var(--paper); }
  body { font-family: "Roboto", Arial, sans-serif; color: var(--ink); }
  .brochure { position: relative; width: 1200px; height: 848px; background: var(--paper); overflow: hidden; }
  .abs { position: absolute; }

  /* Left panel */
  .panel-left { left: 0; top: 0; width: 400px; height: 848px; }
  .section-heading { position: absolute; left: 40px; font-weight: 300; font-size: 19.5px; color: var(--accent); letter-spacing: 0.3px; }
  .body-copy { position: absolute; left: 40px; width: 340px; font-weight: 300; font-size: 14px; line-height: 18.8px; text-align: justify; color: var(--ink); }
  .body-copy p + p { margin-top: 18px; }
  .project-strip { position: absolute; left: 0; top: 286px; width: 400px; height: 106px; }

  /* Middle panel */
  .tagline { position: absolute; left: 420px; font-weight: 300; font-size: 22px; line-height: 26px; letter-spacing: 2.6px; color: var(--ink); text-transform: uppercase; }
  .photo { position: absolute; }
  .services { position: absolute; right: 420px; top: 206px; text-align: right; list-style: none; }
  .services li { font-weight: 300; font-size: 15px; line-height: 19px; letter-spacing: 1.6px; color: var(--ink); text-transform: uppercase; margin-bottom: 18px; }
  .contact { position: absolute; left: 600px; top: 647px; width: 200px; text-align: center; font-size: 13.5px; font-weight: 400; color: var(--ink); }
  .contact .name { color: var(--accent); font-weight: 700; font-size: 17px; letter-spacing: 0.6px; margin-top: 25px; margin-bottom: 18px; }
  .contact .line { margin-bottom: 15px; }
  .contact .line.tight { margin-bottom: 1px; }

  /* Right panel */
  .brand { position: absolute; left: 800px; top: 0; width: 400px; height: 298px; text-align: center; }
  .brand-name { position: absolute; left: 0; width: 400px; top: 184px; font-weight: 700; font-size: 29px; letter-spacing: -0.4px; color: var(--ink-dark); display: flex; justify-content: center; align-items: center; gap: 10px; }
  .brand-dot { width: 14px; height: 14px; border-radius: 50%; background: var(--accent); display: inline-block; }
  .brand-division { position: absolute; left: 0; width: 400px; top: 220px; font-weight: 400; font-size: 11px; letter-spacing: 4.2px; color: var(--muted); text-transform: uppercase; }
  .cover-title { position: absolute; left: 822px; top: 312px; font-weight: 300; font-size: 24px; line-height: 29px; letter-spacing: 2.4px; color: var(--on-photo); text-transform: uppercase; }
  .offer { position: absolute; right: 40px; text-align: right; color: var(--on-photo); }
  .offer h3 { font-weight: 700; font-size: 18px; letter-spacing: 0.3px; text-transform: uppercase; margin-bottom: 3px; }
  .offer li { list-style: none; font-weight: 300; font-size: 15px; line-height: 20.8px; }
</style>
</head>
<body>
<main class="brochure">

  <!-- Left panel -->
  <section class="panel-left abs">
    <h2 class="section-heading" style="top:38px;">MAINTENANCE PROGRAMS</h2>
    <div class="body-copy" style="top:73px;">
      <p>We understand people can be ‘caught up’ or procrastinate in attending to landscape maintenance. Once you have invested in an outdoor project, its important it is retained for continuous enjoyment and longevity, and to avoid any costly neglect!</p>
      <p>As an option, The Ridgewell Craft can set a maintenance program according to your landscape needs addressing various landscaping elements including decking, trees and plants, lighting and so forth.</p>
    </div>

    <svg class="project-strip" viewBox="0 0 400 106" role="img" aria-label="Strip of four project photos: design render, crane on site, garden wall, finished lawn">
      <defs>
        <linearGradient id="stripA" x1="0" y1="0" x2="0" y2="1"><stop offset="0" stop-color="#d9d6d0"/><stop offset="1" stop-color="#8d8a84"/></linearGradient>
        <linearGradient id="stripB" x1="0" y1="0" x2="0" y2="1"><stop offset="0" stop-color="#aac6e2"/><stop offset="1" stop-color="#5e4a3a"/></linearGradient>
        <linearGradient id="stripC" x1="0" y1="0" x2="0" y2="1"><stop offset="0" stop-color="#c9cfc4"/><stop offset="1" stop-color="#6d8a4c"/></linearGradient>
        <linearGradient id="stripD" x1="0" y1="0" x2="0" y2="1"><stop offset="0" stop-color="#b9cbd8"/><stop offset="1" stop-color="#5f8a3d"/></linearGradient>
      </defs>
      <polygon points="0,0 98,0 86,106 0,106" fill="url(#stripA)"/>
      <polygon points="103,0 199,0 187,106 91,106" fill="url(#stripB)"/>
      <polygon points="204,0 299,0 287,106 192,106" fill="url(#stripC)"/>
      <polygon points="304,0 400,0 400,106 292,106" fill="url(#stripD)"/>
    </svg>

    <h2 class="section-heading" style="top:417px;">THE PROCESS</h2>
    <div class="body-copy" style="top:454px;">
      <p>TRC can work with an existing design or create a landscape design to suit your needs.</p>
      <p>Once a design has been established, Dale Harcourt will go over your plans onsite and discuss the requirements to suit your space and climate and provide advice as needed.</p>
      <p>This is followed by a detailed quote which Dale invests his time to breakdown the construction elements and ensure a quality outcome for each stage.</p>
      <p>Dale will project-manage your entire outdoor construction and ensure you are updated throughout the journey.</p>
      <p>Our clients will experience honesty, integrity, and professionalism throughout the project which allows them to embrace their outdoor living after completion.</p>
    </div>
  </section>

  <!-- Middle panel -->
  <h2 class="tagline" style="top:40px;">Landscaping<br>to<br>your<br>lifestyle</h2>

  <svg class="photo" style="left:600px;top:0;" width="200" height="200" role="img" aria-label="Photo of a two-storey house with a lit swimming pool at dusk">
    <defs><linearGradient id="poolPhoto" x1="0" y1="0" x2="0" y2="1"><stop offset="0" stop-color="#27456f"/><stop offset="0.45" stop-color="#c9b99c"/><stop offset="1" stop-color="#1f7fd0"/></linearGradient></defs>
    <rect width="200" height="200" fill="url(#poolPhoto)"/>
  </svg>

  <svg class="photo" style="left:400px;top:201px;" width="200" height="223" role="img" aria-label="Photo of a garden path with stepping stones set in white gravel beside a lawn">
    <defs><linearGradient id="pathPhoto" x1="0" y1="0" x2="0" y2="1"><stop offset="0" stop-color="#4d6a38"/><stop offset="0.45" stop-color="#6aa83f"/><stop offset="0.65" stop-color="#8d8a84"/><stop offset="1" stop-color="#d7d2c8"/></linearGradient></defs>
    <rect width="200" height="223" fill="url(#pathPhoto)"/>
  </svg>

  <ul class="services">
    <li>Consultation<br>and design</li>
    <li>Earthwork &amp; site<br>preparation</li>
    <li>Installation &amp;<br>construction</li>
    <li>Maintenance<br>programs</li>
  </ul>

  <h2 class="tagline" style="top:460px;">Landscape<br>consulting<br>and<br>design</h2>

  <svg class="photo" style="left:600px;top:424px;" width="200" height="222" role="img" aria-label="Photo of a paved courtyard with white outdoor chairs and a round table">
    <defs><linearGradient id="courtPhoto" x1="0" y1="0" x2="0" y2="1"><stop offset="0" stop-color="#9fb58a"/><stop offset="0.5" stop-color="#8c8c86"/><stop offset="1" stop-color="#4e4a45"/></linearGradient></defs>
    <rect width="200" height="222" fill="url(#courtPhoto)"/>
  </svg>

  <svg class="photo" style="left:400px;top:647px;" width="200" height="201" role="img" aria-label="Photo of a front garden entry with slate wall, white planter and paved steps">
    <defs><linearGradient id="entryPhoto" x1="0" y1="0" x2="1" y2="1"><stop offset="0" stop-color="#3e4346"/><stop offset="0.5" stop-color="#6b7a5a"/><stop offset="1" stop-color="#a9a69e"/></linearGradient></defs>
    <rect width="200" height="201" fill="url(#entryPhoto)"/>
  </svg>

  <address class="contact" style="font-style:normal;">
    <div class="name">DALE HARCOURT</div>
    <div class="line">0400 18 36 92</div>
    <div class="line">PO Box 248, Kingsfield 3190</div>
    <div class="line tight">dale@theridgewellcraft.com.au</div>
    <div class="line">www.theridgewellcraft.com.au</div>
  </address>

  <!-- Right panel -->
  <header class="brand">
    <div class="brand-name"><span class="brand-dot"></span>The Ridgewell Craft</div>
    <div class="brand-division">Premier Branch</div>
  </header>

  <svg class="photo" style="left:800px;top:298px;" width="400" height="550" role="img" aria-label="Photo of a slate feature wall with a white planter and floating concrete steps over a lawn">
    <defs><linearGradient id="coverPhoto" x1="0" y1="0" x2="0" y2="1"><stop offset="0" stop-color="#5c6367"/><stop offset="0.5" stop-color="#7d8582"/><stop offset="0.7" stop-color="#cfcdc6"/><stop offset="0.9" stop-color="#b4b2aa"/><stop offset="1" stop-color="#4f7a33"/></linearGradient></defs>
    <rect width="400" height="550" fill="url(#coverPhoto)"/>
  </svg>

  <h1 class="cover-title">Landscape consulting<br>and design</h1>

  <div class="offer" style="top:422px;">
    <h3>Construction</h3>
    <ul><li>Bespoke Structural Features</li><li>Water Features</li><li>Paving &amp; Pathways</li><li>Concreting and Aggregate</li></ul>
  </div>
  <div class="offer" style="top:596px;">
    <h3>Garden</h3>
    <ul><li>Plant &amp; Tree supply &amp; installation</li><li>Earth Preparation</li><li>Lawns</li><li>Irrigation Systems</li></ul>
  </div>
  <div class="offer" style="top:761px;">
    <h3>Maintenance</h3>
    <ul><li>Garden &amp; Structural</li></ul>
  </div>

</main>
</body>
</html>
```